Recipe Card Design

I have a small kitchen store in Livingston Montana, and I would like to have recipe cards (4x6 postcard) designed with my logo, lines for recipe writing, all in black and white. My website is here: www.brambleforkpantry.com

Store

```html
<!DOCTYPE html>
<html lang="en">
<head>
<meta charset="utf-8">
<title>Bramble Fork Pantry Recipe Card</title>
<link rel="stylesheet" href="https://fonts.googleapis.com/css2?family=Anton&family=Poppins:wght@400&display=swap">
<style>
  :root {
    --ink: #111111;
    --paper: #ffffff;
    --panel: #efefef;
    --rule: #2a2a2a;
  }
  html, body {
    margin: 0;
    padding: 0;
    width: 1200px;
    height: 929px;
    overflow: hidden;
    background: var(--paper);
  }
  .card {
    position: relative;
    width: 1200px;
    height: 929px;
    background: var(--paper);
    color: var(--ink);
  }
  .cut-line {
    position: absolute;
    left: 42px; top: 40px;
    width: 1114px; height: 850px;
    box-sizing: border-box;
    border: 3px dashed var(--ink);
  }
  .panel {
    position: absolute;
    background: var(--panel);
    border-radius: 20px;
  }
  .panel--title { left: 304px; top: 52px; width: 820px; height: 148px; }
  .panel--ingredients { left: 288px; top: 223px; width: 836px; height: 207px; }
  .panel--instructions { left: 60px; top: 463px; width: 1072px; height: 389px; }

  .heading-row {
    position: absolute;
    display: flex;
    align-items: baseline;
    gap: 6px;
    margin: 0;
    right: 84px;
  }
  .heading-row--recipe { left: 312px; top: 58px; }
  .heading-row--ingredients { left: 300px; top: 252px; }
  .heading-row--instructions { left: 74px; top: 474px; }

  .heading {
    font-family: "Anton", sans-serif;
    font-weight: 400;
    text-transform: uppercase;
    line-height: 1;
    letter-spacing: 0.5px;
    color: var(--ink);
    white-space: nowrap;
  }
  .heading-row--recipe .heading { font-size: 58px; letter-spacing: 1px; }
  .heading-row--ingredients .heading,
  .heading-row--instructions .heading { font-size: 30px; }

  .utensils { width: 22px; height: 22px; flex: none; }
  .heading-row--recipe .utensils { width: 28px; height: 28px; margin-right: 6px; }

  .heading-row .row-rule {
    flex: 1;
    height: 0;
    margin-left: 8px;
    border-bottom: 2px dotted var(--rule);
  }

  .write-line {
    position: absolute;
    height: 0;
    border-bottom: 2px dotted var(--rule);
  }

  .brand {
    position: absolute;
    left: 66px; top: 116px;
    width: 202px; height: 242px;
    display: flex;
    flex-direction: column;
    align-items: center;
    justify-content: center;
    gap: 14px;
  }
  .brand-mark {
    width: 34px; height: 34px;
    background: var(--ink);
  }
  .brand-name {
    font-family: "Anton", sans-serif;
    font-size: 34px;
    line-height: 1.1;
    text-align: center;
    text-transform: uppercase;
    color: var(--ink);
  }
  .site {
    position: absolute;
    right: 54px; top: 858px;
    font-family: "Poppins", sans-serif;
    font-size: 21px;
    line-height: 1;
    color: var(--ink);
  }
</style>
</head>
<body>
<div class="card">
  <div class="cut-line"></div>

  <div class="brand">
    <div class="brand-mark"></div>
    <div class="brand-name">Bramble<br>Fork<br>Pantry</div>
  </div>

  <div class="panel panel--title"></div>
  <div class="panel panel--ingredients"></div>
  <div class="panel panel--instructions"></div>

  <h1 class="heading-row heading-row--recipe">
    <svg class="utensils" viewBox="0 0 24 24" aria-hidden="true"><g stroke="#111" stroke-width="2.4" stroke-linecap="round" fill="none"><line x1="5" y1="5" x2="20" y2="20"/><line x1="19" y1="5" x2="4" y2="20"/><path d="M3 3 L7 7 M6 2 L8 6"/></g><ellipse cx="18.5" cy="5.5" rx="3" ry="2.2" transform="rotate(-45 18.5 5.5)" fill="#111"/></svg>
    <span class="heading">Recipe</span>
    <span class="row-rule"></span>
  </h1>
  <div class="write-line" style="left:358px; top:188px; width:758px;"></div>

  <h2 class="heading-row heading-row--ingredients">
    <svg class="utensils" viewBox="0 0 24 24" aria-hidden="true"><g stroke="#111" stroke-width="2.4" stroke-linecap="round" fill="none"><line x1="5" y1="5" x2="20" y2="20"/><line x1="19" y1="5" x2="4" y2="20"/><path d="M3 3 L7 7 M6 2 L8 6"/></g><ellipse cx="18.5" cy="5.5" rx="3" ry="2.2" transform="rotate(-45 18.5 5.5)" fill="#111"/></svg>
    <span class="heading">Ingredients</span>
    <span class="row-rule"></span>
  </h2>
  <div class="write-line" style="left:304px; top:340px; width:812px;"></div>
  <div class="write-line" style="left:304px; top:413px; width:812px;"></div>

  <h2 class="heading-row heading-row--instructions">
    <svg class="utensils" viewBox="0 0 24 24" aria-hidden="true"><g stroke="#111" stroke-width="2.4" stroke-linecap="round" fill="none"><line x1="5" y1="5" x2="20" y2="20"/><line x1="19" y1="5" x2="4" y2="20"/><path d="M3 3 L7 7 M6 2 L8 6"/></g><ellipse cx="18.5" cy="5.5" rx="3" ry="2.2" transform="rotate(-45 18.5 5.5)" fill="#111"/></svg>
    <span class="heading">Instructions</span>
    <span class="row-rule"></span>
  </h2>
  <div class="write-line" style="left:86px; top:569px; width:1030px;"></div>
  <div class="write-line" style="left:86px; top:635px; width:1030px;"></div>
  <div class="write-line" style="left:86px; top:705px; width:1030px;"></div>
  <div class="write-line" style="left:86px; top:773px; width:1030px;"></div>
  <div class="write-line" style="left:86px; top:842px; width:1030px;"></div>

  <div class="site">www.brambleforkpantry.com</div>
</div>
</body>
</html>
```